Cybersecurity company is looking for business card.

I need a business card design for our company, we are a cybersecurity company providing advance technology to protect agains any kind of malware. We need a fresh modern design it should communicate modern, technology and growth.

Target Market(s)

Business to business

Industry/Entity Type

Business

Contact Information for Business Card

Should have location, address, fax, mobile, phone, email and website.

Requirements
Must have
• Must follow company's logo color and style. Must have the company's log on its.

```html
<!DOCTYPE html>
<html lang="en">
<head>
<meta charset="utf-8">
<title>Ostrivel Business Card</title>
<link rel="stylesheet" href="https://fonts.googleapis.com/css2?family=Open+Sans:wght@400;600;700;800&display=swap">
<style>
  :root {
    --backdrop: #4a3628;
    --card: #f6f6f4;
    --brand-red: #a51e22;
    --ink: #111111;
    --text-grey: #4a4a4a;
    --white: #ffffff;
  }
  * { margin: 0; padding: 0; box-sizing: border-box; }
  html, body { width: 1200px; height: 480px; overflow: hidden; }
  body {
    background: var(--backdrop);
    font-family: "Open Sans", Arial, sans-serif;
    position: relative;
  }
  .card {
    position: absolute;
    top: 95px;
    width: 476px;
    height: 272px;
    background: var(--card);
    box-shadow: 0 2px 6px rgba(0,0,0,0.35);
    overflow: hidden;
  }
  .card--front { left: 107px; }
  .card--back { left: 637px; }

  .front-band { position: absolute; left: 0; top: 0; width: 170px; height: 272px; }
  .location {
    position: absolute; left: 0; width: 142px; top: 124px;
    text-align: center;
    color: var(--white); font-weight: 700; font-size: 13px; white-space: nowrap;
  }
  .contact-line {
    position: absolute; right: 26px; top: 19px;
    font-size: 12px; color: var(--text-grey); white-space: nowrap;
  }
  .contact-line .label { color: var(--brand-red); font-weight: 700; }
  .contact-line .item + .item { margin-left: 8px; }

  .wordmark {
    font-weight: 800; color: var(--ink);
    line-height: 1; white-space: nowrap;
  }
  .card--front .wordmark {
    position: absolute; left: 196px; top: 100px; font-size: 46px;
  }
  .address {
    position: absolute; right: 48px; top: 219px;
    font-size: 12px; color: var(--text-grey); white-space: nowrap;
  }
  .web-line {
    position: absolute; right: 26px; top: 240px;
    font-size: 12px; color: var(--text-grey); white-space: nowrap;
    display: flex; align-items: center; gap: 5px;
  }
  .web-line svg { width: 11px; height: 11px; }
  .web-line .site { font-weight: 700; color: #333; }
  .web-line .gap { width: 2px; }

  .back-content {
    position: absolute; left: 0; right: 0; top: 68px; text-align: center;
  }
  .card--back .wordmark { font-size: 56px; }
  .person-name {
    margin-top: 10px; color: var(--brand-red);
    font-size: 15px; font-weight: 600;
  }
  .person-title { color: var(--brand-red); font-size: 12px; margin-top: 0; }
</style>
</head>
<body>
  <section class="card card--front">
    <svg class="front-band" viewBox="0 0 170 272" aria-hidden="true">
      <defs>
        <linearGradient id="silver" x1="0" y1="0" x2="1" y2="1">
          <stop offset="0" stop-color="#d9d9d9"/>
          <stop offset="0.35" stop-color="#8e8e8e"/>
          <stop offset="0.5" stop-color="#f4f4f4"/>
          <stop offset="0.75" stop-color="#9a9a9a"/>
          <stop offset="1" stop-color="#e6e6e6"/>
        </linearGradient>
      </defs>
      <polygon points="73,0 100,0 162,136 100,272 73,272 148,136" fill="url(#silver)"/>
      <polygon points="0,0 73,0 148,136 73,272 0,272" fill="var(--brand-red)"/>
    </svg>
    <div class="location">Northbay - UAE</div>

    <div class="contact-line">
      <span class="item"><span class="label">M:</span> +971 50 000 XXXX</span>
      <span class="item"><span class="label">T:</span> 04 000 XXXX</span>
      <span class="item"><span class="label">F:</span> 04 000 XXXX</span>
    </div>

    <div class="wordmark">ostrivel</div>

    <div class="address">Harbor Tech Park (HTP) - Coastal Avenue.</div>
    <div class="web-line">
      <svg viewBox="0 0 12 12" aria-hidden="true">
        <rect x="0.5" y="2" width="11" height="8" fill="var(--brand-red)"/>
        <polyline points="0.5,2 6,6.5 11.5,2" fill="none" stroke="#fff" stroke-width="1"/>
      </svg>
      <span>name.surname@ostrivel.com</span>
      <span class="gap"></span>
      <svg viewBox="0 0 12 12" aria-hidden="true">
        <circle cx="6" cy="6" r="5.3" fill="none" stroke="var(--brand-red)" stroke-width="1.3"/>
        <ellipse cx="6" cy="6" rx="2.3" ry="5.3" fill="none" stroke="var(--brand-red)" stroke-width="1"/>
        <line x1="0.7" y1="6" x2="11.3" y2="6" stroke="var(--brand-red)" stroke-width="1"/>
      </svg>
      <span class="site">www.ostrivel.com</span>
    </div>
  </section>

  <section class="card card--back">
    <div class="back-content">
      <div class="wordmark">ostrivel</div>
      <div class="person-name">Your Name Here</div>
      <div class="person-title">Designation</div>
    </div>
  </section>
</body>
</html>
```